Morvela Aesthetic Doctor

I require an elegant, luxurious looking business card for my aesthetic business. I am a doctor and that will set me aside from competitors. I am planning to provide home and spa based treatments to clients with high expectations. I have attached my logo.

```html
<!DOCTYPE html>
<html lang="en">
<head>
<meta charset="utf-8">
<title>Morvela Aesthetic Doctor – Business Card</title>
<link rel="stylesheet" href="https://fonts.googleapis.com/css2?family=Montserrat:wght@400;500&display=swap">
<style>
  :root {
    --backdrop: #dedfe4;
    --card: #fbfbfb;
    --brand-blue: #3b8dcd;
    --accent-blue: #2f7fc4;
    --mark-blue: #7cc3ea;
    --ink: #333338;
    --rule: #4a9ad6;
  }
  * { margin: 0; padding: 0; box-sizing: border-box; }
  html, body {
    width: 1200px; height: 800px; overflow: hidden;
    background: var(--backdrop);
    font-family: "Montserrat", sans-serif;
    color: var(--ink);
  }
  .card {
    position: absolute;
    left: 390px; width: 460px; height: 263px;
    background: var(--card);
  }
  .card--front { top: 93px; }
  .card--back { top: 422px; }

  .brand {
    position: absolute;
    display: flex; align-items: center;
    color: var(--brand-blue);
    font-weight: 400;
  }
  .brand__dot {
    border-radius: 50%;
    background: var(--mark-blue);
    flex: none;
  }
  .brand__name { line-height: 1; }
  .brand__word { display: block; letter-spacing: 0.08em; }
  .brand__title { display: block; letter-spacing: 0.06em; }

  .card--front .brand { left: 0; right: 0; top: 55px; justify-content: center; gap: 14px; }
  .card--front .brand__dot { width: 70px; height: 70px; }
  .card--front .brand__word { font-size: 38px; }
  .card--front .brand__title { font-size: 15.5px; margin-top: 8px; }

  .card--back .brand { right: 27px; top: 30px; gap: 11px; }
  .card--back .brand__dot { width: 56px; height: 56px; }
  .card--back .brand__word { font-size: 30px; }
  .card--back .brand__title { font-size: 12.3px; margin-top: 6px; }

  .services {
    position: absolute; left: 0; right: 0; top: 186px;
    text-align: center; font-size: 11px; line-height: 13.5px;
  }
  .tagline {
    position: absolute; left: 0; right: 0; top: 213px;
    text-align: center; font-size: 14.5px; color: var(--accent-blue);
  }

  .doctor { position: absolute; left: 25px; top: 150px; }
  .doctor__name { font-size: 13px; font-weight: 500; color: var(--accent-blue); }
  .doctor__letters { font-size: 7px; color: var(--ink); font-weight: 400; margin-left: 2px; }
  .doctor__diploma { font-size: 11.2px; margin-top: 2px; }

  .divider {
    position: absolute; left: 25px; right: 26px; top: 191px;
    height: 1px; background: var(--rule);
  }

  .contacts { position: absolute; left: 26px; top: 199px; list-style: none; font-size: 11px; }
  .contacts li { display: flex; align-items: center; gap: 6px; height: 13.5px; }
  .contacts svg { width: 8px; height: 8px; fill: var(--accent-blue); }

  .follow { position: absolute; right: 26px; top: 207px; text-align: right; font-size: 11px; }
  .follow__links { display: flex; gap: 6px; justify-content: flex-end; margin-top: 8px; }
  .follow__dot { width: 8px; height: 8px; border-radius: 50%; background: var(--accent-blue); }
</style>
</head>
<body>
  <section class="card card--front">
    <div class="brand">
      <span class="brand__dot"></span>
      <span class="brand__name">
        <span class="brand__word">MORVELA</span>
        <span class="brand__title">AESTHETIC DOCTOR</span>
      </span>
    </div>
    <p class="services">Dermal injectables - Plasma facials - Microneedling<br>Skin boosters - Excessive sweating</p>
    <p class="tagline">Home and Spa Based Treatments</p>
  </section>

  <section class="card card--back">
    <div class="brand">
      <span class="brand__dot"></span>
      <span class="brand__name">
        <span class="brand__word">MORVELA</span>
        <span class="brand__title">AESTHETIC DOCTOR</span>
      </span>
    </div>
    <div class="doctor">
      <p class="doctor__name">Dr Elise Marwen <span class="doctor__letters">MRCPCH MD</span></p>
      <p class="doctor__diploma">Australasian Diploma of Aesthetic Medicine</p>
    </div>
    <div class="divider"></div>
    <ul class="contacts">
      <li><svg viewBox="0 0 10 10"><path d="M2 0.5 L3.6 0.5 L4.2 3 L3 3.8 Q4 6.2 6.2 7 L7 5.8 L9.5 6.4 L9.5 8 Q9.5 9.5 8 9.5 Q1 9 0.5 2 Q0.5 0.5 2 0.5Z"/></svg>0800 555 014</li>
      <li><svg viewBox="0 0 10 10"><path d="M0.5 2 H9.5 V8.5 H0.5Z M0.5 2 L5 5.5 L9.5 2" fill="none" stroke="currentColor" style="stroke:var(--accent-blue)"/></svg>elise@morvela.co.nz</li>
      <li><svg viewBox="0 0 10 10" fill="none" style="stroke:#7aa4c8;fill:none"><circle cx="5" cy="5" r="4.3"/><ellipse cx="5" cy="5" rx="2" ry="4.3"/><path d="M0.7 5 H9.3"/></svg>www.morvela.co.nz</li>
    </ul>
    <div class="follow">
      <p>follow</p>
      <div class="follow__links">
        <span class="follow__dot"></span>
        <span class="follow__dot"></span>
      </div>
    </div>
  </section>
</body>
</html>
```